LITTLE DESIGN WORK REQUIRED!

UPDATE: WE WEREN'T OVERLY ECSTATIC WITH THE DESIGNS WE WERE RECEIVING SO WE DID MOST OF THE DESIGN WORK OURSELVES...

PLEASE SEE THE NEWLY ATTACHED PPT DOC TO VIEW NEARLY EXACT REPLICAS OF WHAT WE WANT THE SITE TO LOOK LIKE. WE NOW NEED YOUR HELP TO MAKE IT LOOK LIKE SOMETHING WORTHY OF THE WEB.

NO CODING REQUIRED - EXPECTED OUTPUT PSD FILES

Hi everyone!

We're looking for a designer to work their magic for our site! We're a not-for-profit program aimed at helping young people realise their potential!

In the attached PPT file, you'll notice we've already DESIGNED THE ENTIRE SITE IN POWERPOINT. Now, we need YOU to make the small changes we requested in the document as well as design the whole thing in psd.

Any questions, don't hesitate to ask.

Brook-Rise
Updates

We've done about 95% of the design for you. Please fine-tune it. See the newly attached PPT doc for details. 

The best two designs will win. This project closes on Friday - please message us if you are absolutely sure you cannot make the deadline.

Thanks,
Brook-Rise

```html
<!DOCTYPE html>
<html lang="en">
<head>
<meta charset="utf-8">
<title>Brook-Rise</title>
<link href="https://fonts.googleapis.com/css2?family=Open+Sans:ital,wght@0,300;0,400;0,600;0,700;1,400&display=swap" rel="stylesheet">
<style>
:root{
  --ink:#333;
  --muted:#777;
  --green:#5fae0c;
  --green-light:#8bcb2a;
  --dark:#2c2f33;
  --nav:#3a3b3c;
  --navy:#3b5a94;
  --link:#2a4a8c;
  --panel-line:#d9dcd6;
  --page:#eef4e6;
}
*{margin:0;padding:0;box-sizing:border-box}
html,body{width:954px;height:1200px;overflow:hidden}
body{font-family:"Open Sans",Arial,sans-serif;color:var(--ink);background:linear-gradient(#f6f8f2,var(--page) 40%,#eef4e8)}
.canvas{position:relative;width:954px;height:1200px;overflow:hidden}
.abs{position:absolute}
.top-strip{left:0;top:0;width:954px;height:10px;background:#2f3640}
.header{left:0;top:10px;width:954px;height:126px;background:linear-gradient(90deg,#f1f0e4,#e9eedb 60%,#e3ebcf);}
.header-fade{left:520px;top:10px;width:434px;height:126px;background:linear-gradient(180deg,rgba(150,190,90,.18),rgba(200,210,180,.35));}
.brand{left:104px;top:50px;display:flex;align-items:center;gap:8px;font-weight:700;font-size:28px;color:#1f1f1f;letter-spacing:-.5px}
.brand-dot{width:18px;height:18px;border-radius:50%;background:var(--green)}
.connect{left:617px;top:52px;font-size:16px;font-style:italic;color:#222}
.connect b{font-style:normal;font-weight:700}
.social{left:766px;top:51px;display:flex;gap:3px}
.social span{width:21px;height:21px;border-radius:50%;border:2px solid #fff;box-shadow:0 1px 2px rgba(0,0,0,.3)}
.social .s1{background:#3fb4e6}.social .s2{background:#2d5aa6}.social .s3{background:#f07d1a}.social .s4{background:#1c7fb6}
.nav{left:84px;top:113px;width:787px;height:42px;border-radius:6px 6px 4px 4px;background:linear-gradient(#4a4b4c,#2e2f30);box-shadow:0 2px 3px rgba(0,0,0,.3)}
.nav a{position:absolute;top:13px;font-size:10px;color:#fff;text-decoration:none;letter-spacing:.2px}
.nav .home{left:19px;top:8px;width:42px;height:19px;background:#fff;border:1px solid var(--green-light);color:var(--green);text-align:center;line-height:17px}
.search{left:620px;top:7px;width:148px;height:19px;border-radius:10px;background:#fff;overflow:hidden}
.search span{position:absolute;left:10px;top:3px;font-size:8px;font-style:italic;color:#aaa}
.search i{position:absolute;right:0;top:0;width:24px;height:19px;background:var(--green-light)}
.hero{left:95px;top:148px;width:767px;height:260px;background:linear-gradient(100deg,#c9b4a2,#a08270 30%,#b9a99a 55%,#d8d6d2 80%,#e6e6e6)}
.signup{left:614px;top:204px;width:230px;height:148px;background:#fff;border-radius:4px;box-shadow:0 0 4px rgba(0,0,0,.2);padding:4px}
.signup-frame{width:100%;height:100%;border:4px solid transparent;border-image:repeating-linear-gradient(45deg,#f4a9b3 0 6px,#fff 6px 9px,#a9d6ee 9px 15px,#fff 15px 18px) 4;position:relative}
.signup h2{position:absolute;left:8px;top:6px;font-weight:300;font-size:20px;color:#1d2a5a}
.signup label{position:absolute;left:18px;font-size:7px;color:#222}
.signup .field{position:absolute;left:94px;width:90px;height:14px;border:1px solid #bbb;background:#fff}
.signup .btn{position:absolute;left:94px;top:132px;width:82px;height:18px;border:1px solid #bbb;border-radius:3px;background:linear-gradient(#f7f7f7,#ddd);font-size:10px;color:#444;text-align:center;line-height:16px}
.panel{left:94px;top:422px;width:774px;height:711px;background:linear-gradient(#fff 40%,#f0f0f0);border:1px solid var(--panel-line);border-radius:4px}
.panel-rule{left:95px;top:726px;width:772px;height:1px;background:var(--panel-line)}
h1.welcome{left:106px;top:428px;font-weight:300;font-size:31px;color:#333;letter-spacing:-.5px}
h1.welcome em{font-style:normal;font-weight:400;color:var(--green)}
.intro{left:105px;width:500px;font-size:10.5px;line-height:15px;color:#333}
.intro b{font-weight:600;font-size:17px;color:var(--green);margin-right:4px}
.steps{left:103px;top:587px}
.readmore{left:104px;top:632px;font-size:10px;color:#222}
.section-title{font-weight:300;font-size:27px;color:#333;letter-spacing:-.5px}
.fb-title{left:652px;top:428px;color:var(--navy)}
.fb-box{left:652px;top:470px;width:199px;height:192px;border:1px solid #b9c2d3;background:linear-gradient(#fff,#f2f2f2)}
.fb-head{height:18px;background:var(--navy);color:#fff;font-size:8px;padding:4px 6px;display:flex;justify-content:space-between}
.fb-head b{font-weight:700}
.fb-item{position:absolute;left:6px;width:190px}
.fb-item i{position:absolute;left:0;top:2px;width:18px;height:20px;background:linear-gradient(#4d76c0,#2a4a8c);border-radius:2px}
.fb-item p{margin-left:25px;font-size:8.5px;line-height:10px;color:var(--link)}
.fb-item small{display:block;margin-left:25px;margin-top:3px;font-size:7.5px;color:#555}
.post-title{left:110px;font-size:14px;color:#333}
.post-meta{left:111px;font-size:6.5px;color:#222}
.post-text{left:287px;width:336px;font-size:9px;line-height:12.7px;color:#777}
.photo-run{left:110px;top:782px;width:165px;height:109px;background:linear-gradient(160deg,#7ea65a,#4f6f3a 50%,#575a5c)}
.photo-group{left:112px;top:954px;width:126px;height:142px;background:radial-gradient(ellipse at center,#c8a988 0,#8c7a66 45%,rgba(255,255,255,0) 70%)}
.amb-title{left:654px;top:690px}
.amb{position:absolute;left:654px;width:200px}
.amb .pic{position:absolute;left:0;top:0;width:42px;height:40px;background:linear-gradient(#c6a789,#8a6a54)}
.amb .name{position:absolute;left:51px;top:1px;font-size:10px;color:#222}
.amb .role{position:absolute;left:51px;top:15px;font-size:8.5px;font-style:italic;color:#999}
.amb .meet{position:absolute;left:47px;top:27px;font-size:8.5px;color:#888}
.top-title{left:654px;top:916px}
.tp{position:absolute;left:653px;width:210px}
.tp .pic{position:absolute;left:0;top:0;width:43px;height:40px;background:linear-gradient(#d7c2ad,#7b6453)}
.tp a{position:absolute;left:52px;top:12px;font-size:9px;font-style:italic;color:#444;text-decoration:underline}
.footer{left:0;top:1144px;width:954px;height:56px;background:#1e1f20}
.footer nav{position:absolute;left:0;top:14px;width:954px;text-align:center;font-size:9px}
.footer nav a{color:#999;text-decoration:none;margin:0 9px}
.footer p{position:absolute;left:0;top:30px;width:954px;text-align:center;font-size:9.5px;color:#aaa}
</style>
</head>
<body>
<div class="canvas">
  <div class="abs top-strip"></div>
  <div class="abs header"></div>
  <div class="abs header-fade" role="img" aria-label="Faint silhouettes of a cheering crowd with green splashes"></div>

  <div class="abs brand"><span class="brand-dot"></span>Brook-Rise</div>
  <div class="abs connect">let's stay <b>Connected!</b></div>
  <div class="abs social"><span class="s1"></span><span class="s2"></span><span class="s3"></span><span class="s4"></span></div>

  <nav class="abs nav">
    <a class="home" href="#">HOME</a>
    <a href="#" style="left:116px">ABOUT US</a>
    <a href="#" style="left:226px">RESOURCES</a>
    <a href="#" style="left:342px">WORKSHOPS</a>
    <a href="#" style="left:464px">AMBASSADORS FEATS</a>
    <div class="abs search"><span>search...</span><i></i></div>
  </nav>

  <div class="abs hero" role="img" aria-label="Photo of a smiling group of young people giving thumbs up"></div>
  <form class="abs signup">
    <div class="signup-frame">
      <h2>Sign up</h2>
      <label style="top:50px">Email Address:</label><span class="field" style="top:46px"></span>
      <label style="top:70px">Password:</label><span class="field" style="top:66px"></span>
      <label style="top:90px">Confirm Password</label><span class="field" style="top:86px"></span>
      <span class="btn" style="top:106px">Sign up Now</span>
    </div>
  </form>

  <div class="abs panel"></div>
  <div class="abs panel-rule"></div>

  <h1 class="abs welcome">Welcome to <em>Brook-Rise</em></h1>
  <p class="abs intro" style="top:486px"><b>Brook-Rise</b>is a not-for -profit program aimed at helping people especially young people - realise their potential and achieve success</p>
  <p class="abs intro" style="top:535px"><b>Our resources</b>are categorised into four groups: discovery, design, build and achieve - the four steps in our achievement framework</p>

  <svg class="abs steps" width="410" height="38" viewBox="0 0 410 38">
    <defs><linearGradient id="stepLight" x1="0" y1="0" x2="0" y2="1"><stop offset="0" stop-color="#fafafa"/><stop offset="1" stop-color="#e4e4e4"/></linearGradient></defs>
    <path d="M300 0H398L408 19L398 37H300L310 19Z" fill="url(#stepLight)" stroke="#ccc"/>
    <path d="M200 0H298L308 19L298 37H200L210 19Z" fill="url(#stepLight)" stroke="#ccc"/>
    <path d="M100 0H198L208 19L198 37H100L110 19Z" fill="url(#stepLight)" stroke="#ccc"/>
    <path d="M0 0H98L108 19L98 37H0Z" fill="#3c4148"/>
    <rect x="8" y="9" width="32" height="19" fill="#fff"/>
    <rect x="10" y="15" width="28" height="5" fill="#3f8fd6"/>
    <text x="47" y="23" font-family="Open Sans, sans-serif" font-size="12" fill="#fff">Discover</text>
    <path d="M123 27L133 9L141 27Z" fill="#4a90d0"/><rect x="119" y="27" width="26" height="3" fill="#666"/>
    <text x="151" y="23" font-family="Open Sans, sans-serif" font-size="12" fill="#333">Design</text>
    <rect x="222" y="14" width="20" height="14" fill="#e7a93a"/><path d="M220 15L232 6L244 15Z" fill="#4a76b8"/>
    <text x="256" y="23" font-family="Open Sans, sans-serif" font-size="12" fill="#333">Build</text>
    <path d="M322 30V8" stroke="#666" stroke-width="2"/><path d="M323 8H340L336 14L340 20H323Z" fill="#6aa7dc"/>
    <text x="348" y="23" font-family="Open Sans, sans-serif" font-size="12" fill="#333">Achieve</text>
  </svg>
  <p class="abs readmore">&gt;&gt;&nbsp; Read more</p>

  <h2 class="abs section-title fb-title">Chatterly</h2>
  <div class="abs fb-box">
    <div class="fb-head"><span>Recently Activity</span><b>chatterly</b></div>
    <div class="fb-item" style="top:26px"><i></i><p>Calling All enterpreneurs - Come Hack with Us!</p><small>1,891 people shared this</small></div>
    <div class="fb-item" style="top:66px"><i></i><p>Platform Updates:Improved Dev site, documentation,and more</p><small style="margin-top:7px">1,891 people shared this</small></div>
    <div class="fb-item" style="top:112px"><i></i><p>Calling All enterpreneurs - Come Hack with Us!</p><small>1,891 people shared this</small></div>
    <div class="fb-item" style="top:152px"><i></i><p>Platform Updates:Improved Dev site, documentation,and more</p><small style="margin-top:7px">1,891 people shared this</small></div>
  </div>

  <h2 class="abs section-title" style="left:105px;top:686px">Recent Post</h2>

  <h3 class="abs post-title" style="top:738px;font-weight:400">Studying In The US Without a Car</h3>
  <p class="abs post-meta" style="top:760px">Posted on March 31st, 2012 by Daniel Marsh</p>
  <div class="abs photo-run" role="img" aria-label="Photo of a runner's feet in sneakers on a path"></div>
  <p class="abs post-text" style="top:789px">Lorem Ipsum is simply dummy text of the printing and typesetting industry. Lorem Ipsum has been the industry's standard dummy text ever since the 1500s, when an unknown printer took a galley of type and scrambled it to make a type specimen book. It has survived not only five centuries, but also the leap into electronic typesetting, remaining essentially unchanged. It was popularised in the 1960s with the release of Typeline sheets containing Lorem Ipsum passages, and more recently with desktop publishing software like Draftwell PageSetter including versions of Lorem Ipsum.</p>

  <h3 class="abs post-title" style="top:918px;font-weight:400">International&nbsp; Health Insurance</h3>
  <p class="abs post-meta" style="top:939px">Posted on March 31st, 2012 by Daniel Marsh</p>
  <div class="abs photo-group" role="img" aria-label="Photo of three students standing together with bags and books"></div>
  <p class="abs post-text" style="top:995px">Lorem Ipsum is simply dummy text of the printing and typesetting industry. Lorem Ipsum has been the industry's standard dummy text ever since the 1500s, when an unknown printer took a galley of type and scrambled it to make a type specimen book. It has survived not only five centuries, but also the leap into electronic typesetting, remaining essentially unchanged. It was popularised in the 1960s with the release of Typeline sheets containing Lorem Ipsum passages, and more recently with desktop publishing software like Draftwell PageSetter including versions of Lorem Ipsum.</p>

  <h2 class="abs section-title amb-title">Ambassadors</h2>
  <div class="amb" style="top:744px"><div class="pic" role="img" aria-label="Portrait photo of ambassador"></div><span class="name">John Doe</span><span class="role">Young entrepreneur</span><span class="meet">▸ Meet John</span></div>
  <div class="amb" style="top:796px"><div class="pic" role="img" aria-label="Portrait photo of ambassador"></div><span class="name" style="left:54px">Jane Smith</span><span class="role">Pro athlete</span><span class="meet">▸ Meet Jane</span></div>
  <div class="amb" style="top:846px"><div class="pic" role="img" aria-label="Portrait photo of ambassador"></div><span class="name">John Doe</span><span class="role">Young entrepreneur</span><span class="meet">▸ Meet John</span></div>

  <h2 class="abs section-title top-title">Top Posts</h2>
  <div class="tp" style="top:977px"><div class="pic" role="img" aria-label="Post thumbnail photo"></div><a href="#">Studying In The US Without a Car</a></div>
  <div class="tp" style="top:1030px"><div class="pic" role="img" aria-label="Post thumbnail photo"></div><a href="#" style="top:16px">International Students in South</a></div>
  <div class="tp" style="top:1083px"><div class="pic" role="img" aria-label="Post thumbnail photo"></div><a href="#" style="top:10px">Contrary to popular belief</a></div>

  <footer class="abs footer">
    <nav><a href="#">Home</a><a href="#">About us</a><a href="#">Resources</a><a href="#">Workshops</a><a href="#">Ambassadors</a><a href="#">Feats</a></nav>
    <p>© 2012 Brook-Rise</p>
  </footer>
</div>
</body>
</html>
```